Pest Control - Brolga Pest Management

Pest Control
Termites (white ants)
Cockroaches
Ants
Spiders
Bed Bugs
Rats & Mice
Bird Proofing
Termite Inspections
Termite Baiting
Pest Identification

Commercial Services
Integrated Pest Management
Scheduled Servicing
Stored Product Pest
Rodent & Bird Control

Pre - Construction
Physical Termite Barriers
Chemical Barrier Installation
Reticulation Termite Barriers

Industry/Entity Type

Construction

Contact Information for Business Card

Malcolm: 0412 738 261
Tess: 0419 582 047

```html
<!DOCTYPE html>
<html lang="en">
<head>
<meta charset="utf-8">
<title>Brolga Pest Management – Business Card</title>
<link rel="stylesheet" href="https://fonts.googleapis.com/css2?family=Open+Sans:wght@400;600&display=swap">
<style>
  :root {
    --page-bg: #e9e7e3;
    --card-shadow: rgba(0,0,0,0.28);
    --photo-light: #f4f5f7;
    --photo-mid: #dcdfe3;
    --photo-warm: #c9a58a;
    --band-dark: #3d63a8;
    --band-light: #5d82c4;
    --band-text: #ffffff;
    --back-yellow: #d9b23a;
    --back-red: #e0606a;
    --back-green: #1fa34a;
    --heading-yellow: #f4ea12;
    --item-white: #ffffff;
    --silhouette: rgba(255,255,255,0.22);
  }
  * { box-sizing: border-box; margin: 0; padding: 0; }
  html, body {
    width: 1200px; height: 900px; overflow: hidden;
    background: var(--page-bg);
    font-family: "Open Sans", Arial, sans-serif;
  }
  .sheet {
    width: 1200px; height: 900px;
    display: flex; flex-direction: column;
    align-items: center; justify-content: center; gap: 36px;
  }
  .card {
    position: relative;
    width: 700px; height: 400px;
    border-radius: 4px; overflow: hidden;
    box-shadow: 0 6px 18px var(--card-shadow);
  }

  /* Front */
  .card-front { background: var(--photo-light); }
  .front-photo {
    position: absolute; left: 0; top: 0; width: 100%; height: 322px;
    display: block;
  }
  .contact-band {
    position: absolute; left: 0; bottom: 0; width: 100%; height: 78px;
    display: flex;
  }
  .contact {
    display: flex; align-items: center;
    color: var(--band-text);
    font-size: 27px; font-weight: 400; letter-spacing: 0.5px;
    text-transform: uppercase;
    padding-left: 26px;
  }
  .contact-primary { width: 56%; background: var(--band-dark); }
  .contact-secondary { width: 44%; background: var(--band-light); padding-left: 22px; }

  /* Back */
  .card-back {
    background:
      radial-gradient(ellipse at 52% 48%, var(--back-red) 0%, rgba(224,96,106,0.55) 30%, rgba(224,96,106,0) 62%),
      linear-gradient(150deg, var(--back-yellow) 0%, #d98b55 35%, #b48a4c 60%, var(--back-green) 100%);
  }
  .back-motif {
    position: absolute; left: 250px; top: 60px; width: 200px; height: 290px;
  }
  .service-groups {
    position: absolute; inset: 0;
    display: grid; grid-template-columns: 1fr 1fr;
    padding: 34px 40px;
  }
  .service-group h2 {
    color: var(--heading-yellow);
    font-size: 26px; font-weight: 400; text-transform: uppercase;
    letter-spacing: 0.5px; line-height: 1.1; margin-bottom: 6px;
  }
  .service-group ul { list-style: none; }
  .service-group li {
    color: var(--item-white);
    font-size: 17px; line-height: 1.4;
  }
  .column-right { display: flex; flex-direction: column; justify-content: space-between; padding-left: 40px; }
</style>
</head>
<body>
<main class="sheet">

  <section class="card card-front" aria-label="Business card front">
    <svg class="front-photo" viewBox="0 0 700 322" preserveAspectRatio="none" role="img"
         aria-label="Photo of two hands sheltering a small white house, with cockroaches, a mouse, a spider and an ant beside it">
      <defs>
        <linearGradient id="photoTone" x1="0" y1="0" x2="1" y2="1">
          <stop offset="0" stop-color="#ffffff"/>
          <stop offset="0.55" stop-color="#e7e9ec"/>
          <stop offset="1" stop-color="#d4d7db"/>
        </linearGradient>
        <radialGradient id="pestTone" cx="0.78" cy="0.45" r="0.35">
          <stop offset="0" stop-color="#c9a58a" stop-opacity="0.45"/>
          <stop offset="1" stop-color="#c9a58a" stop-opacity="0"/>
        </radialGradient>
      </defs>
      <rect width="700" height="322" fill="url(#photoTone)"/>
      <rect width="700" height="322" fill="url(#pestTone)"/>
    </svg>
    <div class="contact-band">
      <p class="contact contact-primary">Malcolm: 0412 738 261</p>
      <p class="contact contact-secondary">Tess: 0419 582 047</p>
    </div>
  </section>

  <section class="card card-back" aria-label="Business card back">
    <svg class="back-motif" viewBox="0 0 200 290" role="img" aria-label="Faint white termite silhouette">
      <ellipse cx="100" cy="150" rx="70" ry="130" fill="var(--silhouette)"/>
    </svg>
    <div class="service-groups">
      <div class="service-group">
        <h2>Pest Control</h2>
        <ul>
          <li>Termites (white ants)</li>
          <li>Cockroaches</li>
          <li>Ants</li>
          <li>Spiders</li>
          <li>Bed Bugs</li>
          <li>Rats &amp; Mice</li>
          <li>Bird Proofing</li>
          <li>Termite Inspections</li>
          <li>Termite Baiting</li>
          <li>Pest Identification</li>
        </ul>
      </div>
      <div class="column-right">
        <div class="service-group">
          <h2>Commercial Services</h2>
          <ul>
            <li>Integrated Pest Management</li>
            <li>Scheduled Servicing</li>
            <li>Stored Product Pest</li>
            <li>Rodent &amp; Bird Control</li>
          </ul>
        </div>
        <div class="service-group">
          <h2>Pre - Construction</h2>
          <ul>
            <li>Physical Termite Barriers</li>
            <li>Chemical Barrier Installation</li>
            <li>Reticulation Termite Barriers</li>
          </ul>
        </div>
      </div>
    </div>
  </section>

</main>
</body>
</html>
```